Marlow Landscaping Landing Page

I require a landing page for my landscaping business.

My business plan revolves around hooking clients with weeding services. Not lawn herbicide sprays, but actual hand weeding and bed maintenance. I've found my niche as most people do not want to do this kind of work. From there I often upsell clients into actual hardscaping or softscaping.

I like things to be clean, concise, and to the point. Not overly flashy, but not so minimal that that it's boring. My logo is a very good example of what I like.

The business is LGBTQ owned and operated. I do not broadcast this but I feel the logo itself, along with the name is usually enough to tip people into assumption. I'm not opposed to color, but I do not want the page to scream "gay". My favourite color is yellow...

I used to be a door to door salesman so I'm doing something different where I want to do all my selling in my first meeting with the client. With this said I do not need a section for "work pictures", as I have photos of my work on my tablet, which I show the client during the consultation.

Ideally i'd like my web site to actually be just a landing page. I'd like room for all the following information within the page;

- description of services;
Weeding of Perennial and Flower Beds
Selective Pruning of Trees and Shrubs
Hedging
Landscape Construction
Landscape Design
Total Lawn Treatment Plans
Landscape Pest Control

- contact information, phone, email
Gerald Hanswick
204-731-4426
ger.hanswick@brelvanyard.com

- "free estimates" somewhere on the page that is either led to by the eye, or very easy to notice and see

- and my slogan which is "dependable, reliable, consistent"

- room for a link to my future ratewell account so they can see reviews from real people

- My Logo present

Any or all of these can be custom made graphics or simply text, whatever looks best

I do not want people to have to search for information throughout. Design it in such a way that either the eye flows naturally from one piece of information to the other, or that it's all compartmentalized neatly enough that everything is easy to find.

As I am a landscape and outdoor maintenance service I'm no opposed to images such as flowers, trees, landscaping, etc being present. However please note that my main focus and source of income comes from weeding services, everything else is bonus cash.

Many of my clients are extremely wealthy individuals who pay over $1000 for the season for me just to show up and pull weeds. So making the website appeal to wealthy people as opposed to the average joe is paramount.

I do not cut grass. Please do not have any indication on the website, either through writing or graphics that implies that I cut grass. There are enough companies doing that.

Target Market(s)

Wealthy, often elderly individuals.

Industry/Entity Type

Landscape Gardening

Coding

Coded - Design and coding required

Number of Pages Required

1 page

Font styles to use
Sans Serif

Colors

Designer to choose colors to be used in the design.

Requirements
Must have
• - description of services;
• Weeding of Perennial and Flower Beds
• Selective Pruning of Trees and Shrubs
• Hedging
• Landscape Construction
• Landscape Design
• Total Lawn Treatment Plans
• Landscape Pest Control
• - contact information, phone, email
• Gerald Hanswick
• 204-731-4426
• ger.hanswick@brelvanyard.com
• - "free estimates" somewhere on the page that is either led to by the eye, or very easy to notice and see
• - and my slogan which is "dependable, reliable, consistent"
• - room for a link to my future ratewell account so they can see reviews from real people
• - My Logo present
Nice to have
• Flowers or weeds depicted. Possibly some hardscaping and softscaping if it doesnt look too bulky and crowded.
Should not have
• grass

```html
<!DOCTYPE html>
<html lang="en">
<head>
<meta charset="utf-8">
<title>Marlow Landscaping</title>
<link rel="stylesheet" href="https://fonts.googleapis.com/css2?family=Raleway:wght@400;500;600;700&family=Open+Sans:wght@400;600&family=Lora:ital@1&display=swap">
<style>
:root{
  --yellow:#f5b400;
  --purple:#6a2a7c;
  --orange:#e8842c;
  --green:#2f8a3c;
  --blue:#2e4d9e;
  --red:#d9342b;
  --ink:#222;
  --text:#666;
  --muted:#888;
  --line:#e2e2e2;
  --soft:#f4f5f7;
  --dark:#333;
  --white:#fff;
}
*{box-sizing:border-box;margin:0;padding:0}
html,body{width:1200px;height:2740px;overflow:hidden}
body{position:relative;background:var(--white);font-family:"Open Sans",Arial,sans-serif;color:var(--text)}

/* header */
.site-header{position:absolute;left:0;top:0;width:1200px;height:91px;background:var(--white)}
.top-stripe{position:absolute;left:0;top:0;width:1200px;height:4px;background:linear-gradient(90deg,var(--red),var(--orange),var(--yellow),var(--green),var(--blue),var(--purple))}
.brand{position:absolute;display:flex;align-items:center;gap:9px;font-family:"Raleway",Arial,sans-serif;font-weight:600;color:var(--ink);letter-spacing:.3px;text-transform:uppercase;white-space:nowrap}
.brand-dot{width:15px;height:15px;border-radius:50%;background:var(--yellow)}
.site-header .brand{left:86px;top:37px;font-size:22px}
.main-nav{position:absolute;left:0;top:46px;width:1200px;height:16px;font-family:"Raleway",Arial,sans-serif;font-size:12px;font-weight:500;color:var(--ink);white-space:nowrap}
.main-nav span{position:absolute;top:0}
.main-nav .active{color:var(--yellow)}
.search-btn{position:absolute;left:1066px;top:29px;width:46px;height:46px;border:2px solid var(--yellow);border-radius:50%}
.search-btn svg{position:absolute;left:14px;top:14px}

/* hero */
.hero{position:absolute;left:0;top:91px;width:1200px;height:503px;overflow:hidden}
.hero-photo{position:absolute;inset:0;background:radial-gradient(ellipse at 62% 30%,#b8a78c 0%,rgba(184,167,140,0) 40%),linear-gradient(180deg,#8da45a 0%,#6e8a3e 35%,#5a5238 70%,#3e3426 100%)}
.hero-panel{position:absolute;left:86px;top:270px;width:500px;height:185px;background:rgba(0,0,0,.18)}
.hero-slogan{position:absolute;left:108px;top:287px;color:var(--white);font-family:"Raleway",Arial,sans-serif;font-weight:500;line-height:1.3;text-transform:uppercase}
.hero-slogan .l1{font-size:32px;display:block}
.hero-slogan .l2{font-size:36px;display:block}
.btn-estimate{position:absolute;left:110px;top:390px;width:172px;height:46px;background:var(--yellow);color:var(--white);font-family:"Raleway",Arial,sans-serif;font-weight:700;font-size:17px;text-align:center;line-height:46px;text-transform:uppercase}
.slider-dots{position:absolute;left:568px;top:472px;display:flex;gap:5px}
.slider-dots span{width:16px;height:16px;border:2px solid var(--white);border-radius:50%}
.slider-dots .on{background:rgba(255,255,255,.6)}

/* section titles */
.section-title{position:absolute;left:0;width:1200px;text-align:center;font-family:"Raleway",Arial,sans-serif;font-size:28px;font-weight:400;color:var(--ink);letter-spacing:.5px;display:flex;justify-content:center;align-items:center;gap:10px}
.section-title b{font-weight:700}
.section-title .mark{width:22px;height:22px;border-radius:50%;background:var(--yellow);display:inline-block}
.section-lead{position:absolute;left:0;width:1200px;text-align:center;font-size:11.5px;color:var(--text)}

/* services */
.services{position:absolute;left:0;top:594px;width:1200px;height:959px;background:var(--soft)}
.service-card{position:absolute;width:330px;height:347px;background:var(--white);border:1px solid var(--line);border-bottom:4px solid var(--c);text-align:center}
.service-icon{position:absolute;left:102px;top:13px;width:124px;height:124px;border-radius:50%;background:var(--c)}
.service-name{position:absolute;left:0;top:158px;width:100%;font-family:"Raleway",Arial,sans-serif;font-weight:600;font-size:13px;color:var(--ink);text-transform:uppercase;white-space:nowrap}
.service-text{position:absolute;left:20px;top:190px;width:290px;font-size:11.5px;line-height:24px;color:var(--text)}
.service-more{position:absolute;left:112px;top:280px;width:104px;height:34px;line-height:32px;font-family:"Raleway",Arial,sans-serif;font-weight:600;font-size:13px;text-transform:uppercase;border:1px solid var(--c);color:var(--c)}
.service-more.solid{background:var(--c);color:var(--white)}
.view-all{position:absolute;left:497px;top:884px;width:206px;height:47px;border:1px solid #cfcfcf;background:var(--white);font-family:"Raleway",Arial,sans-serif;font-size:13.5px;color:#555;text-align:center;line-height:45px;text-transform:uppercase}

/* service detail panel */
.detail{position:absolute;left:356px;top:122px;width:705px;height:699px;background:var(--white);border:2px solid var(--purple);padding:50px 0 0 36px}
.detail-close{position:absolute;left:684px;top:-22px;width:42px;height:42px;border-radius:50%;border:2px solid var(--purple);background:var(--white)}
.detail-close svg{position:absolute;left:12px;top:12px}
.detail h3{font-family:"Raleway",Arial,sans-serif;font-weight:600;font-size:22px;color:var(--purple);text-transform:uppercase;margin-bottom:22px}
.detail p{width:620px;font-size:11.5px;line-height:24px;color:var(--text);margin-bottom:14px}
.detail h4{font-family:"Raleway",Arial,sans-serif;font-weight:600;font-size:22px;color:var(--purple);text-transform:uppercase;margin:26px 0 14px}
.features{list-style:none}
.features li{height:37.8px;font-size:11.5px;color:var(--text);display:flex;align-items:flex-start;gap:14px}
.features svg{flex:none;margin-top:3px}

/* reviews */
.reviews{position:absolute;left:0;top:1553px;width:1200px;height:390px}
.review{position:absolute;top:164px;width:300px;height:150px}
.review-badge{position:absolute;left:0;top:0;width:64px;height:64px;border:1px solid var(--line);background:var(--white)}
.review-badge span{position:absolute;left:20px;top:20px;width:24px;height:24px;background:var(--red)}
.review-quote{position:absolute;left:84px;top:0;width:216px;font-size:11.5px;line-height:22px;color:var(--text)}
.review-quote b{font-family:"Lora",serif;font-style:italic;font-size:20px;color:var(--muted);margin-right:4px;line-height:10px}
.review-name{position:absolute;left:84px;top:101px;font-size:11px;font-weight:600;color:var(--yellow);text-transform:uppercase}
.review-meta{position:absolute;left:84px;top:124px;display:flex;align-items:center;gap:8px;font-size:11.5px;color:var(--text)}
.stars{display:flex;gap:2px}
.stars span{width:14px;height:14px;background:var(--orange);border-radius:2px;position:relative}
.stars span.half{background:linear-gradient(90deg,var(--orange) 50%,#ccc 50%)}
.stars svg{position:absolute;left:2px;top:2px}
.divider{position:absolute;left:86px;top:1912px;width:1028px;height:1px;background:var(--line)}

/* blog */
.blog{position:absolute;left:0;top:1943px;width:1200px;height:468px}
.post{position:absolute;top:94px;width:331px}
.post-photo{width:331px;height:197px}
.post-title{margin-top:32px;font-family:"Raleway",Arial,sans-serif;font-weight:600;font-size:15px;color:var(--ink);text-transform:uppercase}
.post-text{margin-top:14px;font-size:11.5px;line-height:22px;color:var(--text)}
.post-meta{margin-top:14px;display:flex;gap:16px;font-family:"Lora",serif;font-style:italic;font-size:12px;color:var(--yellow)}
.post-meta span{display:flex;align-items:center;gap:7px}

/* footer */
.site-footer{position:absolute;left:0;top:2411px;width:1200px;height:261px;background:var(--soft)}
.site-footer .brand{left:86px;top:119px;font-size:22px}
.footer-col{position:absolute;top:56px}
.footer-col h5{font-family:"Raleway",Arial,sans-serif;font-weight:500;font-size:16px;color:var(--ink);text-transform:uppercase;margin-bottom:24px}
.contact-list{list-style:none}
.contact-list li{display:flex;gap:14px;font-size:11.5px;color:var(--muted);height:29px;align-items:flex-start}
.contact-list svg{flex:none;margin-top:2px}
.contact-list .email{text-decoration:underline}
.newsletter-text,.follow-text{font-size:11.5px;line-height:20px;color:var(--muted)}
.newsletter-field{margin-top:17px;width:212px;height:33px;border:1px solid #d6d6d6;background:var(--white);font-size:11.5px;color:#555;padding:8px 14px}
.newsletter-btn{margin-top:9px;width:81px;height:28px;background:var(--yellow);color:var(--white);font-size:9.5px;font-weight:600;text-align:center;line-height:28px;text-transform:uppercase}
.social{display:flex;gap:6px;margin-top:22px}
.social span{width:36px;height:36px;border:1.5px solid #c4c4c4;border-radius:50%}
.copyright{position:absolute;left:0;top:2672px;width:1200px;height:68px;background:var(--dark);color:var(--white);font-size:12px;text-align:center;line-height:68px}
</style>
</head>
<body>

<header class="site-header">
  <div class="top-stripe"></div>
  <div class="brand"><span class="brand-dot"></span>Marlow Landscaping</div>
  <nav class="main-nav">
    <span class="active" style="left:482px">HOME</span>
    <span style="left:570px">ABOUT US</span>
    <span style="left:681px">SERVICES</span>
    <span style="left:787px">NEWS</span>
    <span style="left:875px">REVIEWS</span>
    <span style="left:978px">CONTACT US</span>
  </nav>
  <div class="search-btn"><svg width="14" height="14" viewBox="0 0 14 14"><circle cx="6" cy="6" r="4.2" fill="none" stroke="#f5b400" stroke-width="2"/><line x1="9" y1="9" x2="12.5" y2="12.5" stroke="#f5b400" stroke-width="2"/></svg></div>
</header>

<section class="hero">
  <div class="hero-photo" role="img" aria-label="Photo of a gloveless hand pulling a weed with its roots from a planted flower bed"></div>
  <div class="hero-panel"></div>
  <h1 class="hero-slogan"><span class="l1">Dependable,</span><span class="l2">Reliable, Consistent</span></h1>
  <div class="btn-estimate">Free Estimates</div>
  <div class="slider-dots"><span class="on"></span><span></span><span></span></div>
</section>

<section class="services">
  <h2 class="section-title" style="top:36px"><b>OUR</b><span class="mark"></span><span>SERVICES</span></h2>
  <p class="section-lead" style="top:85px">Sed ut perspiciatis unde omnis iste natus error sit voluptatem accusantium doloremque laudantium, totam rem aperiam</p>

  <article class="service-card" style="left:86px;top:131px;--c:var(--purple)">
    <div class="service-icon" role="img" aria-label="Flower icon for weeding of perennial and flower beds"></div>
    <div class="service-name">Weeding of Perennial &amp; Flower Beds</div>
    <p class="service-text">Sed ut perspiciatis unde omnis iste natus error sit voluptatem accusantium doloremque laudantium, totam rem aperi beatae dicta sunt explicabo.</p>
    <div class="service-more solid">Read More</div>
  </article>
  <article class="service-card" style="left:435px;top:131px;--c:var(--red)">
    <div class="service-icon" role="img" aria-label="Pruning shears icon"></div>
    <div class="service-name">Selective Pruning of Trees &amp; Shrubs</div>
    <p class="service-text">Sed ut perspiciatis unde omnis iste natus error sit voluptatem accusantium doloremque laudantium, totam rem aperi beatae dicta sunt explicabo.</p>
    <div class="service-more">Read More</div>
  </article>
  <article class="service-card" style="left:784px;top:131px;--c:var(--orange)">
    <div class="service-icon" role="img" aria-label="Hedge icon"></div>
    <div class="service-name">Hedging</div>
    <p class="service-text">Sed ut perspiciatis unde omnis iste natus error sit volu ptatem accusantium doloremque laudantium, totam rem aperi beatae dicta sunt explicabo.</p>
    <div class="service-more">Read More</div>
  </article>

  <article class="service-card" style="left:86px;top:506px;--c:var(--yellow)">
    <div class="service-icon" role="img" aria-label="Compact loader icon for landscape construction"></div>
    <div class="service-name">Landscape Construction</div>
    <p class="service-text">Sed ut perspiciatis unde omnis iste natus error sit voluptatem accusantium doloremque laudantium, totam rem aperi vitae dicta sunt explicabo.</p>
    <div class="service-more">Read More</div>
  </article>
  <article class="service-card" style="left:435px;top:506px;--c:var(--green)">
    <div class="service-icon" role="img" aria-label="Design plan icon"></div>
    <div class="service-name">Landscape Design</div>
    <p class="service-text">Sed ut perspiciatis unde omnis iste natus error sit voluptatem accusantium doloremque laudantium, totam rem aperi vitae dicta sunt explicabo.</p>
    <div class="service-more">Read More</div>
  </article>
  <article class="service-card" style="left:784px;top:506px;--c:var(--blue)">
    <div class="service-icon" role="img" aria-label="Pest control icon"></div>
    <div class="service-name">Landscape Pest Control</div>
    <p class="service-text">Sed ut perspiciatis unde omnis iste natus error sit volu ptatem accusantium doloremque laudantium, totam rem aperi vitae dicta sunt explicabo.</p>
    <div class="service-more">Read More</div>
  </article>

  <div class="detail">
    <div class="detail-close"><svg width="14" height="14" viewBox="0 0 14 14"><path d="M3 3L11 11M11 3L3 11" stroke="#6a2a7c" stroke-width="2.4"/></svg></div>
    <h3>Weeding of Perennial &amp; Flower Beds</h3>
    <p>Sed ut perspiciatis unde omnis iste natus error sit voluptatem accusantium doloremque laudantium, totam rem aperiam, eaque ipsa quae ab illo inventore veritatis et quasi architecto beatae vitae dicta sunt explicabo. Nemo enim ipsam voluptatem quia voluptas sit aspernatur aut odit aut fugit, sed quia consequuntur magni dolores eos qui ratione veritatis et quasi architecto beatae voluptatem sequi nesciunt.</p>
    <p>Sed ut perspiciatis unde omnis iste natus error sit voluptatem accusantium doloremque laudantium, totam rem aperiam, eaque ipsa quae ab illo inventore veritatis et quasi architecto beatae vitae dicta sunt explicabo. Nemo enim ipsam voluptatem quia voluptas sit aspernatur aut odit aut fugit, sed quia consequuntur magni dolores eos qui ratione veritatis et quasi architecto beatae voluptatem sequi nesciunt.</p>
    <h4>Features</h4>
    <ul class="features">
      <li><svg width="11" height="9" viewBox="0 0 11 9"><path d="M1 4.5L4 7.5L10 1" fill="none" stroke="#6a2a7c" stroke-width="2"/></svg>Sed ut perspiciatis unde omnis iste natus error sit voluptatem</li>
      <li><svg width="11" height="9" viewBox="0 0 11 9"><path d="M1 4.5L4 7.5L10 1" fill="none" stroke="#6a2a7c" stroke-width="2"/></svg>Accusantium doloremque laudantium, totam rem aper iam,</li>
      <li><svg width="11" height="9" viewBox="0 0 11 9"><path d="M1 4.5L4 7.5L10 1" fill="none" stroke="#6a2a7c" stroke-width="2"/></svg>Eaque ipsa quae ab illo inventore veritatis et quasi architecto</li>
      <li><svg width="11" height="9" viewBox="0 0 11 9"><path d="M1 4.5L4 7.5L10 1" fill="none" stroke="#6a2a7c" stroke-width="2"/></svg>Beatae vitae dicta sunt explicabo. Nemo enim ips am</li>
      <li><svg width="11" height="9" viewBox="0 0 11 9"><path d="M1 4.5L4 7.5L10 1" fill="none" stroke="#6a2a7c" stroke-width="2"/></svg>Voluptatem quia voluptas sit aspernatur aut odit aut fugit,</li>
      <li><svg width="11" height="9" viewBox="0 0 11 9"><path d="M1 4.5L4 7.5L10 1" fill="none" stroke="#6a2a7c" stroke-width="2"/></svg>Sed quia consequuntur magni dolores eos qui ratione veritatis</li>
      <li><svg width="11" height="9" viewBox="0 0 11 9"><path d="M1 4.5L4 7.5L10 1" fill="none" stroke="#6a2a7c" stroke-width="2"/></svg>Quasi architecto beatae voluptatem sequi nesciunt.</li>
    </ul>
  </div>

  <div class="view-all">View All Services</div>
</section>

<section class="reviews">
  <h2 class="section-title" style="top:46px"><b>RATEWELL</b><span class="mark"></span><span>REVIEWS</span></h2>
  <p class="section-lead" style="top:96px">Sed ut perspiciatis unde omnis iste natus error sit voluptatem accusantium doloremque laudantium, totam rem aperiam</p>

  <div class="review" style="left:86px">
    <div class="review-badge"><span></span></div>
    <p class="review-quote"><b>“</b>Sed ut perspiciatis unde omnis iste natus error sit voluptatem accusantium doloremque laudantium, totam rem vitae dicta sunt explicabo.</p>
    <div class="review-name">Owen Brackley</div>
    <div class="review-meta"><div class="stars"><span><svg width="10" height="10" viewBox="0 0 10 10"><path d="M5 .5L6.3 3.6L9.6 3.8L7 5.9L7.9 9.1L5 7.3L2.1 9.1L3 5.9L.4 3.8L3.7 3.6Z" fill="#fff"/></svg></span><span><svg width="10" height="10" viewBox="0 0 10 10"><path d="M5 .5L6.3 3.6L9.6 3.8L7 5.9L7.9 9.1L5 7.3L2.1 9.1L3 5.9L.4 3.8L3.7 3.6Z" fill="#fff"/></svg></span><span><svg width="10" height="10" viewBox="0 0 10 10"><path d="M5 .5L6.3 3.6L9.6 3.8L7 5.9L7.9 9.1L5 7.3L2.1 9.1L3 5.9L.4 3.8L3.7 3.6Z" fill="#fff"/></svg></span><span><svg width="10" height="10" viewBox="0 0 10 10"><path d="M5 .5L6.3 3.6L9.6 3.8L7 5.9L7.9 9.1L5 7.3L2.1 9.1L3 5.9L.4 3.8L3.7 3.6Z" fill="#fff"/></svg></span><span class="half"><svg width="10" height="10" viewBox="0 0 10 10"><path d="M5 .5L6.3 3.6L9.6 3.8L7 5.9L7.9 9.1L5 7.3L2.1 9.1L3 5.9L.4 3.8L3.7 3.6Z" fill="#fff"/></svg></span></div>04/July/2017</div>
  </div>
  <div class="review" style="left:453px">
    <div class="review-badge"><span></span></div>
    <p class="review-quote"><b>“</b>Sed ut perspiciatis unde omnis iste natus error sit voluptatem accusantium doloremque laudantium, totam rem vitae dicta sunt explicabo.</p>
    <div class="review-name">Owen Brackley</div>
    <div class="review-meta"><div class="stars"><span><svg width="10" height="10" viewBox="0 0 10 10"><path d="M5 .5L6.3 3.6L9.6 3.8L7 5.9L7.9 9.1L5 7.3L2.1 9.1L3 5.9L.4 3.8L3.7 3.6Z" fill="#fff"/></svg></span><span><svg width="10" height="10" viewBox="0 0 10 10"><path d="M5 .5L6.3 3.6L9.6 3.8L7 5.9L7.9 9.1L5 7.3L2.1 9.1L3 5.9L.4 3.8L3.7 3.6Z" fill="#fff"/></svg></span><span><svg width="10" height="10" viewBox="0 0 10 10"><path d="M5 .5L6.3 3.6L9.6 3.8L7 5.9L7.9 9.1L5 7.3L2.1 9.1L3 5.9L.4 3.8L3.7 3.6Z" fill="#fff"/></svg></span><span><svg width="10" height="10" viewBox="0 0 10 10"><path d="M5 .5L6.3 3.6L9.6 3.8L7 5.9L7.9 9.1L5 7.3L2.1 9.1L3 5.9L.4 3.8L3.7 3.6Z" fill="#fff"/></svg></span><span class="half"><svg width="10" height="10" viewBox="0 0 10 10"><path d="M5 .5L6.3 3.6L9.6 3.8L7 5.9L7.9 9.1L5 7.3L2.1 9.1L3 5.9L.4 3.8L3.7 3.6Z" fill="#fff"/></svg></span></div>04/July/2017</div>
  </div>
  <div class="review" style="left:820px">
    <div class="review-badge"><span></span></div>
    <p class="review-quote"><b>“</b>Sed ut perspiciatis unde omnis iste natus error sit voluptatem accusantium doloremque laudantium, totam rem vitae dicta sunt explicabo.</p>
    <div class="review-name">Owen Brackley</div>
    <div class="review-meta"><div class="stars"><span><svg width="10" height="10" viewBox="0 0 10 10"><path d="M5 .5L6.3 3.6L9.6 3.8L7 5.9L7.9 9.1L5 7.3L2.1 9.1L3 5.9L.4 3.8L3.7 3.6Z" fill="#fff"/></svg></span><span><svg width="10" height="10" viewBox="0 0 10 10"><path d="M5 .5L6.3 3.6L9.6 3.8L7 5.9L7.9 9.1L5 7.3L2.1 9.1L3 5.9L.4 3.8L3.7 3.6Z" fill="#fff"/></svg></span><span><svg width="10" height="10" viewBox="0 0 10 10"><path d="M5 .5L6.3 3.6L9.6 3.8L7 5.9L7.9 9.1L5 7.3L2.1 9.1L3 5.9L.4 3.8L3.7 3.6Z" fill="#fff"/></svg></span><span><svg width="10" height="10" viewBox="0 0 10 10"><path d="M5 .5L6.3 3.6L9.6 3.8L7 5.9L7.9 9.1L5 7.3L2.1 9.1L3 5.9L.4 3.8L3.7 3.6Z" fill="#fff"/></svg></span><span class="half"><svg width="10" height="10" viewBox="0 0 10 10"><path d="M5 .5L6.3 3.6L9.6 3.8L7 5.9L7.9 9.1L5 7.3L2.1 9.1L3 5.9L.4 3.8L3.7 3.6Z" fill="#fff"/></svg></span></div>04/July/2017</div>
  </div>
</section>

<div class="divider"></div>

<section class="blog">
  <h2 class="section-title" style="top:0"><b>LATEST</b><span class="mark"></span><span>BLOG</span></h2>
  <p class="section-lead" style="top:50px">Sed ut perspiciatis unde omnis iste natus error sit voluptatem accusantium doloremque laudantium, totam rem aperiam</p>

  <article class="post" style="left:86px">
    <div class="post-photo" role="img" aria-label="Photo of a garden trowel beside yellow flowers in clay pots" style="background:linear-gradient(135deg,#7a8a3a 0%,#c9a24a 45%,#a8643a 75%,#5b4a30 100%)"></div>
    <div class="post-title">Neque Porro Quisquam</div>
    <p class="post-text">Sed ut perspiciatis unde omnis iste natus error sit voluptatem accusantiumue ipsa beatae vitae dicta sunt explicabo.</p>
    <div class="post-meta"><span><svg width="12" height="12" viewBox="0 0 12 12"><rect x="1" y="2" width="10" height="9" fill="none" stroke="#f5b400" stroke-width="1.3"/><line x1="1" y1="5" x2="11" y2="5" stroke="#f5b400" stroke-width="1.3"/></svg>1 month ago</span><span><svg width="12" height="12" viewBox="0 0 12 12"><path d="M6 1.5C3 1.5 1 3.3 1 5.5C1 6.7 1.6 7.7 2.6 8.4L2 10.8L4.7 9.4C5.1 9.5 5.5 9.5 6 9.5C9 9.5 11 7.7 11 5.5S9 1.5 6 1.5Z" fill="none" stroke="#f5b400" stroke-width="1.2"/></svg>05 Comments</span></div>
  </article>
  <article class="post" style="left:435px">
    <div class="post-photo" role="img" aria-label="Photo of a gloved hand working soil between plants with a hand rake" style="background:linear-gradient(160deg,#c9d49a 0%,#8c7a52 40%,#5e4a32 75%,#3e3222 100%)"></div>
    <div class="post-title">Neque Porro Quisquam</div>
    <p class="post-text">Sed ut perspiciatis unde omnis iste natus error sit voluptatem accusantiumue ipsa beatae vitae dicta sunt explicabo.</p>
    <div class="post-meta"><span><svg width="12" height="12" viewBox="0 0 12 12"><rect x="1" y="2" width="10" height="9" fill="none" stroke="#f5b400" stroke-width="1.3"/><line x1="1" y1="5" x2="11" y2="5" stroke="#f5b400" stroke-width="1.3"/></svg>1 month ago</span><span><svg width="12" height="12" viewBox="0 0 12 12"><path d="M6 1.5C3 1.5 1 3.3 1 5.5C1 6.7 1.6 7.7 2.6 8.4L2 10.8L4.7 9.4C5.1 9.5 5.5 9.5 6 9.5C9 9.5 11 7.7 11 5.5S9 1.5 6 1.5Z" fill="none" stroke="#f5b400" stroke-width="1.2"/></svg>05 Comments</span></div>
  </article>
  <article class="post" style="left:784px">
    <div class="post-photo" role="img" aria-label="Photo of red gloved hands planting seedlings in a garden bed" style="background:linear-gradient(140deg,#6f9a3e 0%,#4d6e2c 40%,#a83a2e 60%,#4a3a28 100%)"></div>
    <div class="post-title">Neque Porro Quisquam</div>
    <p class="post-text">Sed ut perspiciatis unde omnis iste natus error sit voluptatem accusantiumue ipsa beatae vitae dicta sunt explicabo.</p>
    <div class="post-meta"><span><svg width="12" height="12" viewBox="0 0 12 12"><rect x="1" y="2" width="10" height="9" fill="none" stroke="#f5b400" stroke-width="1.3"/><line x1="1" y1="5" x2="11" y2="5" stroke="#f5b400" stroke-width="1.3"/></svg>1 month ago</span><span><svg width="12" height="12" viewBox="0 0 12 12"><path d="M6 1.5C3 1.5 1 3.3 1 5.5C1 6.7 1.6 7.7 2.6 8.4L2 10.8L4.7 9.4C5.1 9.5 5.5 9.5 6 9.5C9 9.5 11 7.7 11 5.5S9 1.5 6 1.5Z" fill="none" stroke="#f5b400" stroke-width="1.2"/></svg>05 Comments</span></div>
  </article>
</section>

<footer class="site-footer">
  <div class="brand"><span class="brand-dot"></span>Marlow Landscaping</div>

  <div class="footer-col" style="left:407px">
    <h5>Contact Us</h5>
    <ul class="contact-list">
      <li><svg width="13" height="12" viewBox="0 0 13 12"><path d="M1 4C1 2 4 1 6.5 1S12 2 12 4L10 5L9 3.5H4L3 5Z M3 6H10V11H3Z" fill="#999"/></svg>204-731-4426 (Phone)</li>
      <li><svg width="13" height="12" viewBox="0 0 13 12"><rect x="3" y="1" width="7" height="4" fill="#999"/><rect x="1" y="5" width="11" height="5" fill="#999"/><rect x="3" y="8" width="7" height="3" fill="#ccc"/></svg>204-731-4426 (Fax)</li>
      <li><svg width="13" height="12" viewBox="0 0 13 12"><rect x="1" y="2" width="11" height="8" fill="#999"/><path d="M1 2L6.5 6.5L12 2" fill="none" stroke="#fff" stroke-width="1"/></svg><span class="email">ger.hanswick@brelvanyard.com</span></li>
      <li><svg width="13" height="13" viewBox="0 0 13 13"><path d="M6.5 1C4.3 1 2.8 2.6 2.8 4.6C2.8 7.4 6.5 12 6.5 12S10.2 7.4 10.2 4.6C10.2 2.6 8.7 1 6.5 1Z" fill="#999"/><circle cx="6.5" cy="4.7" r="1.4" fill="#fff"/></svg><span>57 Lorem Ipsum Dummy Text<br>Lorem Ipsum</span></li>
    </ul>
  </div>

  <div class="footer-col" style="left:658px">
    <h5>Newsletter</h5>
    <p class="newsletter-text">Register Your email address to get<br>information about us</p>
    <div class="newsletter-field">Email Address</div>
    <div class="newsletter-btn">Subscribe</div>
  </div>

  <div class="footer-col" style="left:904px">
    <h5>Follow Us</h5>
    <p class="follow-text">Lorem ipsum dolor sit amet, conse<br>ctetur adipiscing elit. Nulla in purus<br>nibh. Donec ornare</p>
    <div class="social"><span></span><span></span><span></span><span></span><span></span></div>
  </div>
</footer>

<div class="copyright">© Copyright 2017 Marlow Landscaping.All Rights Reserved</div>

</body>
</html>
```